Personal Training Studio Checkin App (or URL based)

I would like a simple web based app built for our  business. We have a training studio with a simple business model. All our clients buy sessions in packages either 4, 8, or 12 at a time. We want something that a trainer can pull up and Check in a client. This will record the date and time the client was checked in, by what trainer, and what type of session. This system will keep track of the following:
Whenever a Client Checks in so it will ‘tick off’ a session on their package (ie- they have gone from 11 sessions left to 10 sessions left)
Track what sessions a particular trainer does so we can pay them at the end of the week and look at who they trained, what type of session and how many
Look at client activity: Every time they check in, Recharge their package, any activity related to the client, even if it was admin – like deleting a session that was mistakenly recorded.
This will keep a database of clients added and all their activity
The pdf I have included lays out how I think it would work and the features I want
I would like this to run off an vornix that we have at our front check in counter. It can be an app or a URL that use.
***THIS PROJECT IS NOT SO MUCH ABOUT DESIGN BUT ABOUT FUNCTIONALITY OF THE APPLICATION. IT MUST HAVE THE FEATURES I HAVE ASKED FOR THAT WORK TOGETHER. I AM WILLING TO PAY A LITTLE MORE AS A BONUS IF YOU CAN ACCOMPLISH THIS. ALSO IF I FIN THE RIGHT PERSON THAT CAN DO THIS I WILL MAKE IT A GUARNTEED PROJECT.

- Functionality and Track and record all the info we need

```html
<!DOCTYPE html>
<html lang="en">
<head>
<meta charset="utf-8">
<title>Corepath – Welcome</title>
<link rel="stylesheet" href="https://fonts.googleapis.com/css2?family=Roboto:wght@400;500&family=Ubuntu:wght@500;700&display=swap">
<style>
  :root {
    --ink: #111827;
    --text: #374151;
    --muted: #4b5563;
    --brand: #ff4a0a;
    --brand-light: #ff8552;
    --brand-icon: #ff6a2a;
    --card-bg: #f7f7f7;
    --line: #ececec;
    --white: #ffffff;
  }
  * { box-sizing: border-box; margin: 0; padding: 0; }
  html, body { width: 1200px; height: 1110px; overflow: hidden; background: var(--white); }
  body { position: relative; font-family: "Roboto", sans-serif; color: var(--text); }

  .site-header {
    position: absolute; left: 0; top: 0; width: 1200px; height: 91px;
    border-bottom: 1px solid var(--line);
  }
  .brand {
    position: absolute; display: flex; align-items: center; gap: 8px;
    font-family: "Ubuntu", sans-serif; font-weight: 700; color: #5a5a5a;
  }
  .brand-mark { width: 14px; height: 14px; background: var(--brand); }
  .site-header .brand { left: 33px; top: 26px; font-size: 34px; }
  .admin-link {
    position: absolute; left: 1010px; top: 37px;
    font-size: 16.5px; color: var(--text); text-decoration: none;
  }

  .welcome-title {
    position: absolute; left: 0; width: 1200px; top: 196px; text-align: center;
    font-family: "Ubuntu", sans-serif; font-weight: 500; font-size: 29px; color: var(--ink);
  }
  .welcome-lead {
    position: absolute; left: 0; width: 1200px; top: 249px; text-align: center;
    font-size: 16.5px; color: var(--text);
  }

  .option {
    position: absolute; top: 355px; width: 276px; height: 237px; border-radius: 33px;
    display: block; text-decoration: none;
  }
  .option-checkin {
    left: 304px; background: var(--card-bg);
    box-shadow: 0 2px 8px rgba(0,0,0,0.08);
  }
  .option-new {
    left: 610px; background: linear-gradient(180deg, var(--brand-light) 0%, var(--brand) 100%);
  }
  .option-icon { position: absolute; left: 79px; top: 41px; width: 118px; height: 118px; }
  .option-checkin .option-icon { border: 1.5px solid #e2e2e2; border-radius: 50%; }
  .option-label {
    position: absolute; left: 0; width: 100%; top: 180px; text-align: center;
    font-family: "Ubuntu", sans-serif; font-weight: 500; font-size: 19px; color: var(--ink);
  }
  .option-new .option-label { color: var(--white); font-weight: 700; }
  .selection-bar {
    position: absolute; left: 400px; top: 613px; width: 85px; height: 3px;
    border-radius: 2px; background: #e6e6e6;
  }

  .site-footer .brand { left: 0; width: 1200px; justify-content: center; top: 795px; font-size: 32px; }
  .copyright {
    position: absolute; left: 0; width: 1200px; top: 866px; text-align: center;
    font-size: 17px; color: var(--text);
  }
  .legal {
    position: absolute; left: 0; width: 1200px; top: 987px; text-align: center;
    font-size: 13px; color: var(--muted);
  }
</style>
</head>
<body>
  <header class="site-header">
    <div class="brand"><span class="brand-mark"></span>Corepath</div>
    <a class="admin-link" href="#">Admin Panel</a>
  </header>

  <main>
    <h1 class="welcome-title">Welcome!</h1>
    <p class="welcome-lead">Please choose one of the options below to get started. Your selection will help us guide you through the next steps.</p>

    <a class="option option-checkin" href="#">
      <svg class="option-icon" viewBox="0 0 118 118" fill="none" stroke="var(--brand-icon)" stroke-width="5" stroke-linecap="round" stroke-linejoin="round">
        <circle cx="46" cy="31" r="6"/>
        <path d="M28 92V66a12 12 0 0 1 12-12h17"/>
        <path d="M45 66h20"/>
        <circle cx="85" cy="31" r="6"/>
        <path d="M85 53c-8 0-12 6-12 14 0 8 3 16 6 24h12c3-8 6-16 6-24 0-8-4-14-12-14z"/>
      </svg>
      <span class="option-label">Client Check In</span>
    </a>

    <a class="option option-new" href="#">
      <svg class="option-icon" viewBox="0 0 118 118" fill="none" stroke="var(--white)" stroke-width="5" stroke-linecap="round" stroke-linejoin="round">
        <circle cx="57" cy="40" r="17"/>
        <path d="M30 95c0-17 12-28 28-28 6 0 10 1 14 3"/>
        <path d="M83 74v22M72 85h22"/>
      </svg>
      <span class="option-label">Add New Client</span>
    </a>
    <div class="selection-bar"></div>
  </main>

  <footer class="site-footer">
    <div class="brand"><span class="brand-mark"></span>Corepath</div>
    <p class="copyright">© 2025 All rights reserved.</p>
    <p class="legal">Use of this website constitutes acceptance of our User Agreement and Privacy Policy.</p>
  </footer>
</body>
</html>
```